Vorimelo Mobile App

We are in need of a design for a mobile application that delivers relevant content to users based on the profile that they enter and based on the answers that they enter in a daily health tracker. There also will be functionality that will allow a user to check the cost of a medical service/ procedure before going to the medical provider (could get a list of providers and costs after entering procedure, service or prescription in a search box). The content will be articles or information that our team will find/develop on a daily basis and put into a database that the app will pull off of. The profile needs to capture age, sex, ethinicity (optional) and then have a list of topics that the user can select to get daily updated information/content. These topics are: Diabetes, Heart Disease, Hypertension, COPD, Back Pain, Weight Management, Depression, Cancer, Wellness Plan. The final design should allow for users to receive helpful health care information every day based on their profile and the answers in the daily health tracker.

Medical

```html
<!DOCTYPE html>
<html lang="en">
<head>
<meta charset="utf-8">
<title>Vorimelo – Feed</title>
<link rel="stylesheet" href="https://fonts.googleapis.com/css2?family=Roboto+Condensed:wght@300;400;700&family=Roboto:wght@400&display=swap">
<style>
  :root {
    --green: #4abe62;
    --page: #e7e7e7;
    --card: #ffffff;
    --card-line: #d9d9d9;
    --title: #1b1b1b;
    --body: #a2a2a2;
    --heart: #d6282b;
    --xray: #f99b0c;
    --health: #7dd12f;
    --services: #2f8ed4;
    --tabbar: #2a2a2a;
    --tab-line: #444444;
    --white: #ffffff;
  }
  * { box-sizing: border-box; margin: 0; padding: 0; }
  html, body { width: 676px; height: 1200px; overflow: hidden; }
  body {
    position: relative;
    background: var(--page);
    font-family: "Roboto Condensed", "Helvetica Neue", Arial, sans-serif;
  }
  .top-bar {
    position: absolute; left: 0; top: 0; width: 676px; height: 135px;
    background: var(--green); color: var(--white);
  }
  .status-bar {
    position: absolute; left: 0; top: 0; width: 100%; height: 42px;
    font-family: "Roboto", Arial, sans-serif; font-size: 22px;
  }
  .status-bar .carrier { position: absolute; left: 8px; top: 8px; display: flex; align-items: center; gap: 4px; }
  .status-bar .signal { display: flex; gap: 3px; margin-right: 6px; }
  .status-bar .signal i { width: 11px; height: 11px; border-radius: 50%; border: 1.5px solid var(--white); }
  .status-bar .signal i.on { background: var(--white); }
  .status-bar .wifi { margin-left: 22px; }
  .status-bar .time { position: absolute; left: 0; right: 0; top: 8px; text-align: center; }
  .status-bar .battery { position: absolute; right: 10px; top: 8px; display: flex; align-items: center; gap: 8px; }
  .battery-cell { width: 46px; height: 20px; border: 2px solid var(--white); border-radius: 4px; padding: 2px; position: relative; }
  .battery-cell::before { content: ""; display: block; width: 100%; height: 100%; background: var(--white); border-radius: 1px; }
  .battery-cell::after { content: ""; position: absolute; right: -6px; top: 5px; width: 3px; height: 7px; background: var(--white); border-radius: 0 2px 2px 0; }
  .brand {
    position: absolute; left: 0; right: 0; top: 58px; text-align: center;
    font-weight: 700; font-size: 40px; letter-spacing: 0.5px; color: var(--white);
  }

  .feed { position: absolute; left: 19px; top: 158px; width: 638px; }
  .article {
    position: absolute; left: 0; width: 638px; height: 211px;
    background: var(--card); border: 1px solid var(--card-line);
  }
  .topic { position: absolute; left: 0; top: 0; width: 170px; height: 100%; text-align: center; }
  .topic-badge {
    position: absolute; left: 31px; top: 30px; width: 110px; height: 110px; border-radius: 50%;
    display: flex; align-items: center; justify-content: center;
  }
  .topic-name { position: absolute; left: 0; width: 170px; top: 152px; font-family: "Roboto", Arial, sans-serif; font-weight: 400; font-size: 27px; }
  .article-title {
    position: absolute; left: 176px; top: 28px; right: 16px;
    font-weight: 400; font-size: 31px; color: var(--title); white-space: nowrap;
  }
  .article-excerpt {
    position: absolute; left: 176px; top: 80px; right: 20px;
    font-weight: 300; font-size: 25px; line-height: 34px; color: var(--body);
    text-align: justify;
    display: -webkit-box; -webkit-line-clamp: 3; -webkit-box-orient: vertical; overflow: hidden;
  }
  .topic-heart .topic-badge { background: var(--heart); } .topic-heart .topic-name { color: var(--heart); }
  .topic-xray .topic-badge { background: var(--xray); } .topic-xray .topic-name { color: var(--xray); }
  .topic-health .topic-badge { background: var(--health); } .topic-health .topic-name { color: var(--health); }
  .topic-services .topic-badge { background: var(--services); } .topic-services .topic-name { color: var(--services); }

  .tab-bar {
    position: absolute; left: 0; top: 1096px; width: 676px; height: 104px;
    background: var(--tabbar); display: flex;
  }
  .tab {
    width: 225.33px; height: 100%; position: relative; color: var(--white);
    font-family: "Roboto", Arial, sans-serif; font-size: 21px; text-align: center;
    border-left: 1px solid var(--tab-line);
  }
  .tab:first-child { border-left: none; }
  .tab.is-active { background: var(--green); }
  .tab svg { position: absolute; left: 50%; top: 18px; transform: translateX(-50%); }
  .tab .tab-label { position: absolute; left: 0; right: 0; top: 70px; }
</style>
</head>
<body>
  <header class="top-bar">
    <div class="status-bar">
      <div class="carrier">
        <span class="signal"><i class="on"></i><i class="on"></i><i class="on"></i><i></i><i></i></span>
        <span>Nettora</span>
        <svg class="wifi" width="24" height="18" viewBox="0 0 24 18" fill="none" stroke="#fff" stroke-width="2.4" stroke-linecap="round">
          <path d="M2 6a14 14 0 0 1 20 0"/><path d="M6 10a8.5 8.5 0 0 1 12 0"/><circle cx="12" cy="15" r="1.6" fill="#fff" stroke="none"/>
        </svg>
      </div>
      <div class="time">4:21 PM</div>
      <div class="battery"><span>100%</span><span class="battery-cell"></span></div>
    </div>
    <div class="brand">Vorimelo</div>
  </header>

  <main class="feed">
    <article class="article topic-heart" style="top:0">
      <div class="topic">
        <div class="topic-badge">
          <svg width="56" height="50" viewBox="0 0 56 50" fill="none" stroke="#fff" stroke-width="2.6" stroke-linejoin="round">
            <path d="M28 46 C8 32 3 22 3 14 A11.5 11.5 0 0 1 28 9 A11.5 11.5 0 0 1 53 14 C53 22 48 32 28 46Z"/>
          </svg>
        </div>
        <div class="topic-name">Heart</div>
      </div>
      <h2 class="article-title">5 Exercises to Improve Heart Health</h2>
      <p class="article-excerpt">You don’t need to be a hardcore athlete to boost your heart health. Moderate exercise can significantly reduce your risk of heart disease and stroke over time.</p>
    </article>

    <article class="article topic-xray" style="top:230px">
      <div class="topic">
        <div class="topic-badge">
          <svg width="46" height="54" viewBox="0 0 46 54" fill="none" stroke="#fff" stroke-width="2.2" stroke-linecap="round">
            <rect x="3" y="3" width="40" height="48" rx="3"/>
            <path d="M23 9v22"/><path d="M14 14h18M13 19h20M14 24h18"/>
            <path d="M15 35c3-3 13-3 16 0c-2 6-14 6-16 0z"/>
          </svg>
        </div>
        <div class="topic-name">X-ray</div>
      </div>
      <h2 class="article-title">How X-rays Work</h2>
      <p class="article-excerpt">As with many of mankind's monumental discoveries, X-ray technology was invented completely by accident. In 1895, a German physicist was testing cathode rays.</p>
    </article>

    <article class="article topic-health" style="top:459px">
      <div class="topic">
        <div class="topic-badge">
          <svg width="56" height="56" viewBox="0 0 56 56" fill="none" stroke="#fff" stroke-width="2.4" stroke-linecap="round" stroke-linejoin="round">
            <path d="M36 8l12 12"/><path d="M42 14l-6 6"/>
            <path d="M40 18L18 40l-6-2-2-6L32 10z"/>
            <path d="M12 44L5 51"/><path d="M24 26l4 4M28 22l4 4M20 30l4 4"/>
          </svg>
        </div>
        <div class="topic-name">Health</div>
      </div>
      <h2 class="article-title">2-day Free Health Services</h2>
      <p class="article-excerpt">In connection with the National Health Month, the City of ABCDE will hold a week-long free health services to all of its residents this coming month.</p>
    </article>

    <article class="article topic-services" style="top:688px">
      <div class="topic">
        <div class="topic-badge">
          <svg width="58" height="52" viewBox="0 0 58 52" fill="none" stroke="#fff" stroke-width="2.4" stroke-linecap="round" stroke-linejoin="round">
            <path d="M4 40V18h30v22"/><path d="M34 24h10l8 9v7h-18"/>
            <path d="M4 40h6M20 40h14"/>
            <circle cx="15" cy="42" r="5"/><circle cx="43" cy="42" r="5"/>
            <path d="M19 23v10M14 28h10"/>
            <path d="M27 13V9M21 12l-2-3M33 12l2-3"/>
          </svg>
        </div>
        <div class="topic-name">Services</div>
      </div>
      <h2 class="article-title">Sample T</h2>
      <p class="article-excerpt">In connection with the National Health Month, the City of ABCDE will hold a week-long free health services to all of its residents this coming month.</p>
    </article>

    <article class="article" style="top:916px"></article>
  </main>

  <nav class="tab-bar">
    <div class="tab is-active">
      <svg width="48" height="40" viewBox="0 0 48 40" fill="none" stroke="#fff" stroke-width="2" stroke-linecap="round">
        <circle cx="4" cy="4" r="2.5"/><circle cx="4" cy="14" r="2.5"/><circle cx="4" cy="24" r="2.5"/><circle cx="4" cy="34" r="2.5"/>
        <path d="M14 4h32M14 14h32M14 24h32M14 34h32"/>
      </svg>
      <span class="tab-label">Feed</span>
    </div>
    <div class="tab">
      <svg width="54" height="54" viewBox="0 0 54 54" fill="none" stroke="#fff" stroke-width="2.2">
        <circle cx="27" cy="27" r="25"/><circle cx="27" cy="21" r="6"/>
        <path d="M17 37c0-5 4-8 10-8s10 3 10 8c-3 2-17 2-20 0z"/>
      </svg>
      <span class="tab-label">Profile</span>
    </div>
    <div class="tab">
      <svg width="60" height="54" viewBox="0 0 60 54" fill="none" stroke="#fff" stroke-width="2.2">
        <circle cx="10" cy="22" r="6"/><circle cx="30" cy="22" r="6"/><circle cx="50" cy="22" r="6"/>
      </svg>
      <span class="tab-label">More</span>
    </div>
  </nav>
</body>
</html>
```